Need Bold, Hip Card for Concert Ticket Website Gleaming Passes!

Hi there! I am putting together a business/website that sells event tickets (mostly concerts, but also some sports and theater). Think SeatNook, but much smaller. The site is called Gleaming Passes. I have a new logo (attached, with black/red/white color scheme), and am looking for a modern/cool/original business card design. Note that I am thinking of having the card itself in the shape of a ticket (die cut), so you may want to keep that in mind when designing, but I'm not set on that. I'm also open to alternative card sizes, thicknesses, glossy, spot UV, etc. in order to stand out. I'm attaching a potential die cut template and a sample card using that template in case you want to work with that.
Target Market(s)
Music fans, people that like going to see live events
Industry/Entity Type
Entertainment
Contact Information for Business Card
Information that I'd like to have:
website address - www.gleamingpasses.example
phone number: 1-833-5GLEAMNG (532-6264)
my name - Wendel Pike

```html
<!DOCTYPE html>
<html lang="en">
<head>
<meta charset="utf-8">
<title>Gleaming Passes – Business Card</title>
<link rel="stylesheet" href="https://fonts.googleapis.com/css2?family=Montserrat:wght@700&family=Marcellus+SC&family=Arimo:wght@700&display=swap">
<style>
  :root {
    --backdrop: #3a2720;
    --card-white: #ffffff;
    --card-black: #000000;
    --brand-red: #8e0a0a;
    --name-red: #9a0c0c;
    --wave-fill: #5e0808;
    --edge: #d9d6d3;
  }
  * { margin: 0; padding: 0; box-sizing: border-box; }
  html, body { width: 1200px; height: 1000px; overflow: hidden; }
  body { background: var(--backdrop); position: relative; font-family: "Arimo", Arial, sans-serif; }

  .card-art { position: absolute; left: 0; top: 0; width: 1200px; height: 1000px; }

  .wave-placeholder {
    position: absolute;
    background: var(--wave-fill);
  }
  .wave-placeholder--front { left: 550px; top: 332px; width: 110px; height: 102px; }
  .wave-placeholder--back { left: 720px; top: 690px; width: 94px; height: 90px; }

  .brand-mark {
    position: absolute;
    display: flex;
    align-items: center;
    color: var(--brand-red);
    font-family: "Montserrat", Arial, sans-serif;
    font-weight: 700;
    text-transform: uppercase;
    line-height: 0.95;
  }
  .brand-mark__square { background: var(--brand-red); flex: none; }

  .brand-mark--front { left: 330px; top: 110px; gap: 28px; }
  .brand-mark--front .brand-mark__square { width: 100px; height: 100px; }
  .brand-mark--front .brand-mark__name { font-size: 60px; }
  .brand-mark--front .brand-mark__line2 { display: block; font-size: 46px; letter-spacing: 14px; }

  .brand-mark--back { left: 276px; top: 680px; gap: 12px; }
  .brand-mark--back .brand-mark__square { width: 44px; height: 44px; }
  .brand-mark--back .brand-mark__name { font-size: 27px; }
  .brand-mark--back .brand-mark__line2 { display: block; font-size: 21px; letter-spacing: 5px; }

  .holder-name {
    position: absolute;
    left: 558px; width: 407px; top: 596px;
    text-align: center;
    font-family: "Marcellus SC", Georgia, serif;
    font-size: 56px;
    color: var(--name-red);
    letter-spacing: 1px;
    white-space: nowrap;
  }

  .contact-list { position: absolute; left: 586px; top: 786px; list-style: none; }
  .contact-list__item {
    display: flex; align-items: center; gap: 10px;
    height: 28px; margin-bottom: 14px;
    color: var(--card-white); font-size: 21px; font-weight: 700;
    white-space: nowrap;
  }
  .contact-list__icon { width: 28px; height: 28px; flex: none; }
</style>
</head>
<body>

<svg class="card-art" viewBox="0 0 1200 1000" aria-hidden="true">
  <defs>
    <clipPath id="front-inner">
      <path d="M291 72 H911 A40 40 0 0 0 951 112 V424 A40 40 0 0 0 911 464 H291 A40 40 0 0 0 251 424 V112 A40 40 0 0 0 291 72 Z"/>
    </clipPath>
    <clipPath id="back-shape">
      <path d="M282 507 H920 A45 45 0 0 0 965 552 V908 A45 45 0 0 0 920 953 H282 A45 45 0 0 0 237 908 V552 A45 45 0 0 0 282 507 Z"/>
    </clipPath>
  </defs>

  <g class="card-front">
    <path fill="var(--card-white)" stroke="var(--edge)" stroke-width="1.5"
      d="M279 58 H923 A42 42 0 0 0 965 100 V436 A42 42 0 0 0 923 478 H279 A42 42 0 0 0 237 436 V100 A42 42 0 0 0 279 58 Z"/>
    <g clip-path="url(#front-inner)">
      <rect x="240" y="300" width="720" height="170" fill="var(--card-black)"/>
    </g>
    <line x1="253" y1="383" x2="550" y2="383" stroke="var(--brand-red)" stroke-width="4"/>
    <line x1="660" y1="383" x2="948" y2="383" stroke="var(--brand-red)" stroke-width="4"/>
  </g>

  <g class="card-back" clip-path="url(#back-shape)">
    <rect x="237" y="507" width="321" height="446" fill="var(--card-white)"/>
    <rect x="558" y="507" width="407" height="446" fill="var(--card-black)"/>
    <line x1="558" y1="735" x2="720" y2="735" stroke="var(--brand-red)" stroke-width="4"/>
    <line x1="814" y1="735" x2="965" y2="735" stroke="var(--brand-red)" stroke-width="4"/>
  </g>
</svg>

<div class="wave-placeholder wave-placeholder--front" role="img" aria-label="Red sound-wave ornament"></div>
<div class="wave-placeholder wave-placeholder--back" role="img" aria-label="Red sound-wave ornament"></div>

<div class="brand-mark brand-mark--front">
  <span class="brand-mark__square"></span>
  <span class="brand-mark__name">Gleaming<span class="brand-mark__line2">Passes</span></span>
</div>

<div class="brand-mark brand-mark--back">
  <span class="brand-mark__square"></span>
  <span class="brand-mark__name">Gleaming<span class="brand-mark__line2">Passes</span></span>
</div>

<div class="holder-name">Wendel Pike</div>

<ul class="contact-list">
  <li class="contact-list__item">
    <svg class="contact-list__icon" viewBox="0 0 28 28" aria-hidden="true">
      <circle cx="14" cy="14" r="13" fill="var(--brand-red)"/>
      <g fill="none" stroke="var(--card-black)" stroke-width="1.5">
        <circle cx="14" cy="14" r="8"/>
        <ellipse cx="14" cy="14" rx="3.5" ry="8"/>
        <line x1="6" y1="14" x2="22" y2="14"/>
      </g>
    </svg>
    <span>www.gleamingpasses.example</span>
  </li>
  <li class="contact-list__item">
    <svg class="contact-list__icon" viewBox="0 0 28 28" aria-hidden="true">
      <circle cx="14" cy="14" r="13" fill="var(--brand-red)"/>
      <path fill="var(--card-black)" d="M9 7 l3 0 l1.5 4 l-2 1.5 a9 9 0 0 0 4 4 l1.5 -2 l4 1.5 l0 3 a2 2 0 0 1 -2 2 A13 13 0 0 1 7 9 a2 2 0 0 1 2 -2 Z"/>
    </svg>
    <span>1-833-5GLEAMNG (532-6264)</span>
  </li>
</ul>

</body>
</html>
```